Mortgage firm needs clean and simple wordpress website and logo

The competition is for design only, and the winning design for the homepage will be expected to create a second design for a simpler template for additional pages.

We need a logo and basic wordpress website design for a Sydney based mortgage firm.
We need a clean and simple logo and website, based on the mortgage/accounting/finance/tax industry. Simple, credible and official colors.

The logo is expected to be so simple that we have combined into the one job.
If you submit a logo design and we choose it along with someone else's website design you will be paid a bonus of $60. The website design will still win the competition as per normal.

Current website is old and terrible but gives you an idea of the sitemap (super simple) and what they do: http://www.lendbridgeloans.com.au/

We will integrate a mortgage calculator into the site.
The calculator is adjustable in styles, you can see it here: http://www.lendbridgeloans.com.au/mortgagecalculator/

We want original different to copy-and-paste template looking designs.
We like simple websites with a long home page and a few additional pages like https://www.homefundpath.com.au/

We are based in Sydney Australia and are mortgage brokers

We want a clean, formal, credible site, limited pages.

The project is guaranteed, so go for it.

Example of basic template after home page complete: http://lendbridgeloans.com.au/template_example.jpg

Target Market(s)

Mortgage and banking clients

Industry/Entity Type

Finance

Number of Pages Required

1 page

Requirements
Must have
• A simple logo, Wordpress capable, be able to incorporate the mortgage calculator (on the home page if needed as well as its own page)
Nice to have
• VIdeo - something free but nice

```html
<!DOCTYPE html>
<html lang="en">
<head>
<meta charset="utf-8">
<title>Lendbridge Loans</title>
<link href="https://fonts.googleapis.com/css2?family=Lato:wght@300;400;700;900&display=swap" rel="stylesheet">
<style>
:root{
  --blue:#2aa3dc;
  --navy:#1e2a44;
  --ink:#222222;
  --body:#555555;
  --light:#f0f0f0;
  --footer:#161616;
  --white:#ffffff;
  --green:#2ee02e;
}
*{box-sizing:border-box;margin:0;padding:0}
html,body{width:1200px;height:3956px;overflow:hidden}
body{font-family:'Lato',sans-serif;color:var(--body);background:var(--white);position:relative}
section,header,footer{position:relative;width:1200px;overflow:hidden}
.abs{position:absolute}

/* hero */
.hero{height:733px;background:linear-gradient(180deg,#2a3550 0%,#4a5878 40%,#7a7d8e 70%,#3a4155 100%)}
.hero-photo{position:absolute;inset:0;background:radial-gradient(ellipse at 30% 60%,rgba(255,255,255,.18),transparent 50%),radial-gradient(ellipse at 75% 55%,rgba(255,200,140,.15),transparent 45%)}
.brand{position:absolute;left:80px;top:40px;display:flex;align-items:center;gap:12px;color:var(--white);font-size:26px;font-weight:700}
.brand-mark{width:22px;height:22px;background:var(--white);border-radius:50%}
.nav{position:absolute;right:80px;top:70px;display:flex;gap:30px}
.nav a{color:var(--white);text-decoration:none;font-size:14px;font-weight:700;letter-spacing:.5px;padding-bottom:6px}
.nav a.active{border-bottom:2px solid var(--white)}
.hero-copy{position:absolute;top:280px;left:0;width:1200px;text-align:center;color:var(--white)}
.hero-copy .pre{font-size:40px;font-weight:700;letter-spacing:1px}
.hero-copy h1{font-size:54px;font-weight:900;letter-spacing:1px;line-height:1.1}
.hero-copy p{font-size:19px;line-height:1.4;margin-top:16px}
.btn-ghost{display:inline-block;margin-top:30px;border:2px solid var(--white);border-radius:8px;color:var(--white);font-weight:700;font-size:17px;padding:10px 32px;text-decoration:none}

/* features */
.features{height:533px;display:flex;justify-content:center;gap:0}
.feature{width:332px;text-align:center;padding:50px 40px 0}
.feature-icon{width:158px;height:158px;border-radius:50%;margin:0 auto;border:2px dashed #cfcfcf;display:flex;align-items:center;justify-content:center}
.feature-icon span{width:134px;height:134px;border-radius:50%;background:var(--blue);display:flex;align-items:center;justify-content:center}
.feature h3{font-size:24px;color:var(--ink);font-weight:700;margin-top:28px;letter-spacing:.5px}
.feature p{font-size:15.5px;line-height:1.45;margin-top:14px}

/* band */
.band{height:361px;background:linear-gradient(90deg,#5d4a3c 0%,#8a7a68 45%,#6e6356 100%);text-align:center;color:var(--white)}
.band-shade{position:absolute;inset:0;background:rgba(20,20,20,.45)}
.band h2{position:relative;padding-top:74px;font-size:26px;font-weight:700}
.band h2::after{content:"";display:block;width:60px;height:2px;background:var(--white);margin:14px auto 0}
.band p{position:relative;width:1040px;margin:24px auto 0;font-size:15.5px;line-height:1.55}
.band .btn-ghost{position:relative;margin-top:30px;font-size:16px;padding:9px 40px}

/* about */
.about{height:504px}
.about-photo{position:absolute;left:87px;top:74px;width:327px;height:316px;background:linear-gradient(135deg,#3c5a7a,#9fb3c4 55%,#c9a77a)}
.about-tab{position:absolute;left:380px;top:74px;width:34px;height:190px;background:var(--blue);color:var(--white);font-weight:700;font-size:15px;writing-mode:vertical-rl;text-align:center;letter-spacing:12px;line-height:34px}
.about-copy{position:absolute;left:517px;top:70px;width:600px}
.about-copy h2{font-size:46px;font-weight:400;color:var(--ink);letter-spacing:.5px}
.about-copy p{font-size:15.5px;line-height:1.55;margin-top:22px}

/* calculator */
.calc{height:696px;background:linear-gradient(180deg,#e9e9e9,#f4f4f4)}
.calc h2{position:absolute;left:87px;top:84px;font-size:46px;font-weight:400;color:var(--blue);line-height:1.1}
.calc-photo{position:absolute;left:0;top:190px;width:514px;height:396px;background:linear-gradient(135deg,#d9d9d9,#f7f7f7 50%,#c7a35a 80%,#b9423a)}
.field{position:absolute;top:64px}
.field label{display:block;font-size:15px;color:var(--ink);margin-bottom:10px}
.field .box{display:flex;height:32px;border:1px solid #cfcfcf;background:var(--white);font-size:14px;align-items:center}
.field .unit{padding:0 8px;background:#f2f2f2;height:100%;display:flex;align-items:center;border-right:1px solid #cfcfcf}
.field .unit.r{border-right:0;border-left:1px solid #cfcfcf}
.field .val{flex:1;padding:0 8px}
.calc h3{position:absolute;left:551px;top:170px;font-size:24px;color:var(--ink);font-weight:700}
.chart{position:absolute;left:551px;top:216px;width:564px;height:250px;background:var(--white);border:4px solid #bdbdbd}
.sel{position:absolute;top:572px}
.sel label{display:block;font-size:15px;color:var(--ink);margin-bottom:10px}
.sel .box{width:186px;height:34px;border:1px solid #bfbfbf;background:var(--white);font-size:14px;display:flex;align-items:center;padding-left:10px;position:relative}
.sel .box::after{content:"";position:absolute;right:0;top:0;width:22px;height:100%;border-left:1px solid #bfbfbf;background:#eee}

/* media */
.media{height:606px}
.video{position:absolute;left:82px;top:171px;width:503px;height:272px;background:linear-gradient(135deg,#1c1c1c,#5b524a 55%,#2a2a2a)}
.video-bar{position:absolute;left:0;bottom:0;width:100%;height:34px;background:rgba(0,0,0,.75)}
.map{position:absolute;left:614px;top:92px;width:501px;height:430px;background:linear-gradient(135deg,#e4e2de,#d7d3cc 60%,#e9dcc2)}

/* partners */
.partners{height:153px;background:var(--light);display:flex;align-items:center;justify-content:space-between;padding:0 87px}
.badge{height:34px;background:#c9ccd3;border-radius:4px}

/* footer */
.footer{height:370px;background:var(--footer);color:var(--white)}
.footer h4{font-size:17px;font-weight:700;letter-spacing:.5px}
.contact{position:absolute;left:113px;top:50px}
.contact-row{display:flex;align-items:flex-start;gap:12px;margin-top:34px;font-size:14px;line-height:1.6}
.contact-row b{width:70px;font-weight:700}
.links{position:absolute;left:477px;top:50px;width:270px}
.links li{list-style:none;font-size:13px;font-weight:700;padding:13px 0 13px 18px;border-bottom:1px solid #333;position:relative}
.links li::before{content:"";position:absolute;left:2px;top:19px;width:5px;height:5px;border-radius:50%;background:var(--blue)}
.links ul{margin-top:20px}
.social{position:absolute;right:80px;top:50px;text-align:right}
.social-dots{display:flex;gap:12px;justify-content:flex-end;margin-top:24px}
.social-dots span{width:30px;height:30px;border-radius:50%;background:var(--white)}
.social h5{font-size:16px;font-weight:400;margin-top:34px;letter-spacing:.5px}
.newsletter{display:flex;margin-top:20px;height:34px}
.newsletter .in{width:196px;background:var(--white);color:#555;font-size:11px;display:flex;align-items:center;padding-left:10px}
.newsletter .go{background:var(--blue);font-size:11px;font-weight:700;padding:0 10px;display:flex;align-items:center}
.copy{position:absolute;left:113px;top:310px;font-size:13px}
.top-btn{position:absolute;right:80px;top:300px;width:30px;height:30px;background:var(--white)}
</style>
</head>
<body>

<header class="hero">
  <div class="hero-photo" role="img" aria-label="Night skyline of a harbour city with an opera house"></div>
  <div class="brand"><span class="brand-mark"></span>Lendbridge Loans</div>
  <nav class="nav">
    <a class="active" href="#">HOME</a><a href="#">ABOUT</a><a href="#">OUR SERVICES</a><a href="#">CONTACT US</a>
  </nav>
  <div class="hero-copy">
    <div class="pre">WELCOME TO</div>
    <h1>LENDBRIDGE LOANS</h1>
    <p>Home, investment and commercial loans for purchase, refinance<br>and consolidation at up to 80% lending.</p>
    <a class="btn-ghost" href="#">CONTACT US</a>
  </div>
</header>

<section class="features">
  <div class="feature">
    <div class="feature-icon"><span>
      <svg width="70" height="70" viewBox="0 0 70 70" fill="none" stroke="#fff" stroke-width="3"><path d="M15 32 35 14 55 32"/><path d="M22 28v18h26V28"/><rect x="31" y="34" width="8" height="12"/><path d="M8 54c10-6 18-4 26 0h16"/></svg>
    </span></div>
    <h3>EXPERIENCED</h3>
    <p>Lendbridge Loans have been organising and managing money for clients for over 25 years using our access to banks, private lenders and brokers within Australia.</p>
  </div>
  <div class="feature">
    <div class="feature-icon"><span>
      <svg width="70" height="70" viewBox="0 0 70 70" fill="none" stroke="#fff" stroke-width="3"><path d="M35 10 55 18v16c0 13-9 22-20 26-11-4-20-13-20-26V18z"/><circle cx="35" cy="30" r="6" fill="#fff"/><path d="M24 46c2-6 6-9 11-9s9 3 11 9" fill="#fff"/></svg>
    </span></div>
    <h3>PRIVATE</h3>
    <p>Our speciality is private lending for residential, commercial and industrial properties. We generally look for registered first mortgage security with up to 80% loan funding based on the property valuation, the type of security and the borrower profile.</p>
  </div>
  <div class="feature">
    <div class="feature-icon"><span>
      <svg width="74" height="70" viewBox="0 0 74 70" fill="none" stroke="#fff" stroke-width="3"><rect x="24" y="14" width="36" height="20"/><rect x="30" y="34" width="36" height="22"/><text x="48" y="51" fill="#fff" stroke="none" font-size="16" font-family="Lato,sans-serif" text-anchor="middle">$</text><path d="M6 20h12M10 28h10M4 36h18"/></svg>
    </span></div>
    <h3>FAST</h3>
    <p>We can provide money in 24 Hours, providing you meet the loan criteria. Unlike banks that might take months to complete a loan, we can react to your demands quickly.</p>
  </div>
</section>

<section class="band" role="img" aria-label="Small model house with stacked coins on a desk">
  <div class="band-shade"></div>
  <h2>OUR MORTGAGE BROKERS MAKE HOME LOANS EASY</h2>
  <p>We'll do all the paperwork and running around, with expert advice at no cost to you.Lorem Ipsum has been the industry's standard dummy text ever since the 1500s, when an unknown printer took a galley of type and scrambled it to make a type specimen book. It has survived not only five centuries, but also the leap into electronic typesetting, remaining essentially unchanged.</p>
  <a class="btn-ghost" href="#">REACH US</a>
</section>

<section class="about">
  <div class="about-photo" role="img" aria-label="Handshake over a model house and keys"></div>
  <div class="about-tab">ABOUT US</div>
  <div class="about-copy">
    <h2>WE ARE PASSIONATE</h2>
    <p>We have arranged finance for clients over many years through banks, non-bank lenders, mortgage managers and brokers.</p>
    <p>With a lending panel that includes the major banks through to more exclusive lenders, as well as private loan funding, there is a wide choice of finance options to suit your individual requirements.</p>
    <p>We believe it's not just long term employees that should be eligible for finance. Business owners, self-employed borrowers and contractors who are often unfairly dismissed when it comes to bank credit assessment, are welcome to apply with Lendbridge Loans.</p>
  </div>
</section>

<section class="calc">
  <h2>MORTGAGE<br>CALCULATOR</h2>
  <div class="calc-photo" role="img" aria-label="Calculator, pen, coins and a small house model on paperwork"></div>
  <div class="field" style="left:551px;width:130px"><label>Loan Amount</label><div class="box"><span class="unit">$</span><span class="val">100000</span><span class="unit r">AUD</span></div></div>
  <div class="field" style="left:746px;width:130px"><label>Loan Term</label><div class="box"><span class="val">30 years</span><span class="unit r">years</span></div></div>
  <div class="field" style="left:940px;width:162px"><label>Loan Interest</label><div class="box"><span class="val">6%</span><span class="unit r">%</span></div></div>
  <h3>Your repayment would be 600 per month</h3>
  <div class="chart">
    <svg width="556" height="242" viewBox="0 0 556 242" font-family="Lato,sans-serif" font-size="11" fill="#777">
      <g stroke="#e6e6e6"><line x1="60" y1="36" x2="460" y2="36"/><line x1="60" y1="92" x2="460" y2="92"/><line x1="60" y1="148" x2="460" y2="148"/><line x1="60" y1="204" x2="460" y2="204"/></g>
      <text x="52" y="40" text-anchor="end">100,000</text><text x="52" y="96" text-anchor="end">75,000</text><text x="52" y="152" text-anchor="end">50,000</text><text x="52" y="208" text-anchor="end">25,000</text><text x="52" y="232" text-anchor="end">0</text>
      <text x="90" y="236">2020</text><text x="220" y="236">2030</text><text x="345" y="236">2040</text>
      <path d="M60 36C180 40 270 70 330 110S420 200 450 222" stroke="var(--green)" stroke-width="3" fill="none" stroke-dasharray="2 9" stroke-linecap="round"/>
      <circle cx="353" cy="133" r="6" fill="var(--green)"/>
      <rect x="270" y="90" width="125" height="42" fill="#fff" stroke="#ccc"/>
      <text x="280" y="107" fill="#333">Principal remaining:40647</text>
      <text x="280" y="124" fill="#333">Years remaining:7</text>
      <text x="480" y="24" fill="#333">Repayments</text><text x="480" y="38" fill="#333" font-weight="700">215938</text>
      <text x="480" y="60" fill="#333">Interest</text><text x="480" y="74" fill="#333" font-weight="700">115938</text>
    </svg>
  </div>
  <div class="sel" style="left:551px"><label>Repayment Type</label><div class="box">Principal and interest</div></div>
  <div class="sel" style="left:786px"><label>Repayment Frequency</label><div class="box" style="width:124px">Monthly</div></div>
</section>

<section class="media">
  <div class="video" role="img" aria-label="Video still of a couple browsing homes on a tablet">
    <svg class="abs" style="left:224px;top:108px" width="56" height="56" viewBox="0 0 56 56"><circle cx="28" cy="28" r="25" fill="none" stroke="#fff" stroke-width="3"/><path d="M22 17v22l18-11z" fill="#fff"/></svg>
    <div class="video-bar">
      <svg width="503" height="34"><path d="M12 10v14l11-7z" fill="#fff"/><rect x="40" y="15" width="360" height="4" fill="#777"/><rect x="40" y="15" width="150" height="4" fill="#ddd"/><rect x="420" y="11" width="20" height="12" fill="#bbb"/><rect x="452" y="11" width="20" height="12" fill="#bbb"/></svg>
    </div>
  </div>
  <div class="map" role="img" aria-label="Street map with a location pin at the office">
    <svg class="abs" style="left:200px;top:100px" width="30" height="42" viewBox="0 0 30 42"><path d="M15 0C7 0 0 6 0 15c0 11 15 27 15 27s15-16 15-27C30 6 23 0 15 0z" fill="#d9382c"/><circle cx="15" cy="15" r="5" fill="#8e1f17"/></svg>
  </div>
</section>

<section class="partners" aria-label="Lending partners">
  <div class="badge" style="width:114px"></div>
  <div class="badge" style="width:74px"></div>
  <div class="badge" style="width:76px;background:#1d4f91"></div>
  <div class="badge" style="width:100px"></div>
  <div class="badge" style="width:76px"></div>
  <div class="badge" style="width:112px;background:#e9a24a"></div>
  <div class="badge" style="width:122px"></div>
  <div class="badge" style="width:48px"></div>
</section>

<footer class="footer">
  <div class="contact">
    <h4>CONTACT US</h4>
    <div class="contact-row"><svg width="14" height="18" viewBox="0 0 14 18"><path d="M7 0C3 0 0 3 0 7c0 5 7 11 7 11s7-6 7-11c0-4-3-7-7-7z" fill="var(--blue)"/></svg><b>Adress:</b><span>7 street name,<br>City name , Country</span></div>
    <div class="contact-row"><svg width="16" height="16" viewBox="0 0 16 16"><path d="M3 1l3 3-2 2c1 2 3 4 5 5l2-2 3 3-2 3C6 15 1 10 1 3z" fill="var(--blue)"/></svg><b>Phone:</b><span>123-456-789</span></div>
    <div class="contact-row"><svg width="16" height="12" viewBox="0 0 16 12"><rect width="16" height="12" fill="var(--blue)"/><path d="M0 0l8 6 8-6" stroke="#161616" fill="none"/></svg><b>E-mail:</b><span>info@domain.com</span></div>
  </div>
  <div class="links">
    <h4>QUICK LINKS</h4>
    <ul><li>OUR SERVICES</li><li>ABOUT</li><li>OUR CLIENTS</li><li>CONTACT US</li></ul>
  </div>
  <div class="social">
    <h4>STAY CONNECTED</h4>
    <div class="social-dots"><span></span><span></span><span></span></div>
    <h5>SUBSCRIBE OUR NEWSLETTER</h5>
    <div class="newsletter"><div class="in">Enter Your Email Address</div><div class="go">SUBSCRIBE</div></div>
  </div>
  <div class="copy">© 2016 Copyright lendbridge loans. All rights reserved.</div>
  <div class="top-btn"><svg width="30" height="30"><path d="M9 18l6-6 6 6" stroke="#161616" stroke-width="2" fill="none"/></svg></div>
</footer>

</body>
</html>
```